Black Car Limousine transportation business in Naples Florida

Always stand for my reliability and RNT stands for Rest, N and T are the first initials of my children's names. It should show professionalism and a dedication to customer service. We keep our clients identities private. Show our professionalism. We are Black car Black tie company. We service transportation on a reserve basis to and from residents, airports, casinos, hotels,

Target Market(s)

It is a Private car service. High end clients. Businesses, Celebrity and athletes. Service to airports, hotels, special events.

Industry/Entity Type

Business

Contact Information for Business Card

A pearl metallic or Luster card. Standard business card size. Would like the name, Company email, show we take credit cards and phone number. Currently I don't have a website but will like to add later.

Logo Text

STEADFAST RNT TRANSPORTATION

Font styles to use
Serif

Colors
eaeaea
000000

Requirements
Must have
• Must have Company email, show we take credit cards and phone number. Currently I don't have a website but will like to add later.
Nice to have
• Would like to stay with a black and white theme. Open to some color trim.
Should not have
• Open to suggestions

```html
<!DOCTYPE html>
<html lang="en">
<head>
<meta charset="utf-8">
<title>Steadfast RNT Transportation – Business Card</title>
<link href="https://fonts.googleapis.com/css2?family=Signika:wght@300;400;600&display=swap" rel="stylesheet">
<style>
  :root {
    --stage: #d9d6d0;
    --card-black: #1b1b1b;
    --card-white: #ffffff;
    --ink: #1a1a1a;
    --ink-soft: #2b2b2b;
    --gold: #f2b705;
    --muted: #8f8f8f;
    --white: #ffffff;
  }
  * { margin: 0; padding: 0; box-sizing: border-box; }
  html, body { width: 1200px; height: 800px; overflow: hidden; }
  body {
    background: var(--stage);
    font-family: "Signika", sans-serif;
    position: relative;
  }
  .card {
    position: absolute;
    left: 280px;
    width: 640px;
    height: 356px;
  }
  .card--front { top: 30px; background: var(--card-black); }
  .card--back  { top: 410px; background: var(--card-white); }

  /* Front */
  .vehicle-art {
    position: absolute;
    left: 218px; top: 62px;
    width: 194px; height: 104px;
    border-radius: 14px 14px 4px 4px;
    background: linear-gradient(180deg, #d8d8d8 0%, #8a8a8a 45%, #3a3a3a 100%);
  }
  .brand-name {
    position: absolute;
    left: 0; right: 0; top: 182px;
    text-align: center;
    color: var(--white);
    font-weight: 600;
    font-size: 46px;
    letter-spacing: 1px;
    line-height: 1;
  }
  .brand-sub {
    position: absolute;
    left: 0; right: 0; top: 240px;
    text-align: center;
    color: var(--white);
    font-weight: 600;
    font-size: 17px;
    letter-spacing: 1.5px;
  }

  /* Back */
  .tagline {
    position: absolute;
    left: 0; right: 0; top: 32px;
    text-align: center;
    font-weight: 600;
    font-size: 27px;
    color: var(--ink);
    line-height: 1;
  }
  .tagline-sub {
    position: absolute;
    left: 0; right: 0; top: 60px;
    text-align: center;
    font-style: italic;
    font-size: 15.5px;
    color: var(--gold);
  }
  .company {
    position: absolute;
    left: 35px; top: 130px;
    color: var(--ink-soft);
  }
  .company-name { font-weight: 600; font-size: 17px; color: var(--ink); line-height: 1.1; }
  .company-address { font-size: 13.5px; line-height: 1.15; }
  .divider {
    position: absolute;
    left: 35px; top: 189px;
    width: 34px; height: 1.5px;
    background: var(--gold);
  }
  .person {
    position: absolute;
    left: 35px; top: 204px;
  }
  .person-name { font-weight: 600; font-size: 21px; color: var(--ink); line-height: 1.1; }
  .person-title { font-size: 13.5px; color: var(--ink-soft); }
  .contact-list {
    position: absolute;
    left: 35px; top: 256px;
    list-style: none;
    font-size: 13.5px;
    color: var(--ink-soft);
  }
  .contact-list li { display: flex; align-items: center; height: 21px; }
  .contact-icon { width: 18px; height: 18px; margin-right: 9px; }
  .payment-note {
    position: absolute;
    left: 0; right: 0; top: 315px;
    text-align: center;
    font-size: 16px;
    color: var(--muted);
  }
</style>
</head>
<body>
  <section class="card card--front">
    <div class="vehicle-art" role="img" aria-label="Black luxury SUV, front view"></div>
    <div class="brand-name">STEADFAST RNT</div>
    <div class="brand-sub">TRANSPORTATION</div>
  </section>

  <section class="card card--back">
    <h1 class="tagline">WHEREVER YOU WANT TO BE.</h1>
    <p class="tagline-sub">Your right decision when you need a way to go.</p>

    <div class="company">
      <p class="company-name">STEADFAST RNT TRANSPORTATION LLC</p>
      <p class="company-address">4815 Harbor Palm Way, 2206<br>Naples, Florida 34100</p>
    </div>
    <div class="divider"></div>

    <div class="person">
      <p class="person-name">DANIEL MARCHETTI</p>
      <p class="person-title">General Manager</p>
    </div>

    <ul class="contact-list">
      <li>
        <svg class="contact-icon" viewBox="0 0 18 18" aria-hidden="true">
          <circle cx="9" cy="9" r="9" fill="#1a1a1a"/>
          <path d="M6 4.5c.5 0 1.6 2 1.6 2.4 0 .5-.9.9-.9 1.3 0 .7 1.9 2.7 2.7 2.7.4 0 .8-.9 1.3-.9.4 0 2.4 1.1 2.4 1.6 0 .8-1 1.6-1.8 1.6C8.8 13.2 4.8 9.2 4.8 6.3c0-.8.7-1.8 1.2-1.8z" fill="#f2b705"/>
        </svg>
        (877) 555 0142
      </li>
      <li>
        <svg class="contact-icon" viewBox="0 0 18 18" aria-hidden="true">
          <circle cx="9" cy="9" r="9" fill="#1a1a1a"/>
          <rect x="4.8" y="6" width="8.4" height="6" rx="0.6" fill="#f2b705"/>
          <path d="M4.8 6.3 9 9.4l4.2-3.1" fill="none" stroke="#1a1a1a" stroke-width="0.9"/>
        </svg>
        steadfastrnt.rides@example.com
      </li>
    </ul>

    <p class="payment-note">We take your credit card.</p>
  </section>
</body>
</html>
```